Disability and mental health support work company requires business card

Specialising
Wrenfield Disability is a new QCAP service aimed toward QCAP participants with a history of criminal justice, psychosocial/mental health, intellectual, and cognitive disabilities.

Our focus
Focusing on providing core QCAP supports for community participation, daily activities and supported independent living.

Authentic
Likeminded people wanting to make a difference in participant's lives.

Our aim to provide holistic and empowering supports targeted towards creating independence and guidance for all participants and families.
Over 35 years of experience working with people that have psychosocial, intellectual, and cognitive disabilities.

Industry/Entity Type

disability and mental health

Contact Information for Business Card

logo - business name

Colors
0054AA
0677BA
7BADD7
CADEEF
E8F1F8
FFF300
FFF600
FEFA6F
FFFEC7
FFFEE8

Requirements
Must have
• want double sided business cards(wont let me change it)
Should not have
• any disability related pictures

```html
<!DOCTYPE html>
<html lang="en">
<head>
<meta charset="utf-8">
<title>Wrenfield Disability – Business Card</title>
<link rel="stylesheet" href="https://fonts.googleapis.com/css2?family=Source+Sans+3:wght@300;400;600;700&display=swap">
<style>
  :root {
    --navy: #13365c;
    --navy-soft: #1c426d;
    --sun: #f0b91e;
    --sky: #7badd7;
    --white: #ffffff;
    --backdrop: #c9d0d7;
    --shadow: rgba(20, 30, 45, 0.35);
  }
  * { box-sizing: border-box; margin: 0; padding: 0; }
  html, body {
    width: 1200px;
    height: 780px;
    overflow: hidden;
  }
  body {
    background: var(--backdrop);
    font-family: "Source Sans 3", "Helvetica Neue", Arial, sans-serif;
    display: flex;
    align-items: center;
    justify-content: center;
    gap: 40px;
  }
  .card {
    position: relative;
    width: 540px;
    height: 309px;
    background: var(--navy);
    overflow: hidden;
    box-shadow: 0 10px 24px var(--shadow);
  }

  /* Brand lockup: plain circle + name */
  .brand {
    position: absolute;
    display: flex;
    flex-direction: column;
    align-items: center;
    justify-content: center;
    border: 2px solid var(--sky);
    border-radius: 50%;
    color: var(--sky);
    font-weight: 400;
    text-transform: uppercase;
    text-align: center;
  }
  .brand__line { display: block; }

  .card--logo .brand {
    width: 170px;
    height: 170px;
    left: 185px;
    top: 69px;
    font-size: 17px;
    letter-spacing: 0.28em;
    line-height: 1.5;
  }
  .card--logo .brand__line--sub {
    font-size: 9px;
    letter-spacing: 0.4em;
  }

  .card--details .brand {
    width: 84px;
    height: 84px;
    left: 34px;
    top: 34px;
    border-width: 1.5px;
    font-size: 9px;
    letter-spacing: 0.18em;
    line-height: 1.5;
  }
  .card--details .brand__line--sub {
    font-size: 5.5px;
    letter-spacing: 0.3em;
  }

  /* Neutral placeholder for the sunrise illustration */
  .illustration {
    position: absolute;
    left: 60px;
    top: 140px;
    width: 220px;
    height: 95px;
    background: var(--navy-soft);
  }

  .band {
    position: absolute;
    left: 0;
    right: 0;
    bottom: 0;
    height: 74px;
    background: var(--sun);
  }

  .identity {
    position: absolute;
    left: 300px;
    top: 50px;
  }
  .identity__name {
    color: var(--sun);
    font-weight: 700;
    font-size: 30px;
    letter-spacing: 0.01em;
    line-height: 1;
  }
  .identity__role {
    color: var(--white);
    font-weight: 400;
    font-size: 11.5px;
    letter-spacing: 0.04em;
    margin-top: 5px;
  }

  .contacts {
    position: absolute;
    left: 318px;
    top: 128px;
    list-style: none;
  }
  .contacts__item {
    display: flex;
    align-items: center;
    gap: 8px;
    color: var(--white);
    font-size: 12px;
    line-height: 1;
    margin-bottom: 11px;
  }
  .contacts__icon {
    width: 12px;
    height: 12px;
    flex: none;
  }

  .address {
    position: absolute;
    left: 355px;
    bottom: 20px;
    color: var(--navy);
    font-style: normal;
    font-weight: 600;
    font-size: 13px;
    line-height: 1.25;
    text-align: left;
  }
</style>
</head>
<body>

  <section class="card card--logo" aria-label="Business card, logo side">
    <div class="brand">
      <span class="brand__line">Wrenfield</span>
      <span class="brand__line brand__line--sub">Disability</span>
    </div>
  </section>

  <section class="card card--details" aria-label="Business card, contact side">
    <div class="brand">
      <span class="brand__line">Wrenfield</span>
      <span class="brand__line brand__line--sub">Disability</span>
    </div>

    <div class="illustration" role="img" aria-label="Rising sun illustration with radiating rays"></div>
    <div class="band"></div>

    <div class="identity">
      <h1 class="identity__name">MARCUS HALE</h1>
      <p class="identity__role">MANAGING DIRECTOR</p>
    </div>

    <ul class="contacts">
      <li class="contacts__item">
        <svg class="contacts__icon" viewBox="0 0 24 24" aria-hidden="true">
          <path fill="#f0b91e" d="M6.6 10.8a15.1 15.1 0 0 0 6.6 6.6l2.2-2.2a1 1 0 0 1 1-.25 11.4 11.4 0 0 0 3.6.57 1 1 0 0 1 1 1V20a1 1 0 0 1-1 1A17 17 0 0 1 3 4a1 1 0 0 1 1-1h3.5a1 1 0 0 1 1 1c0 1.25.2 2.45.57 3.570a1 1 0 0 1-.25 1z"/>
        </svg>
        +1 555 0142 778
      </li>
      <li class="contacts__item">
        <svg class="contacts__icon" viewBox="0 0 24 24" aria-hidden="true">
          <rect x="2" y="5" width="20" height="14" rx="1.5" fill="#f0b91e"/>
          <path d="M3 6.5l9 6.5 9-6.5" fill="none" stroke="#13365c" stroke-width="1.8"/>
        </svg>
        hello@wrenfield.com
      </li>
      <li class="contacts__item">
        <svg class="contacts__icon" viewBox="0 0 24 24" aria-hidden="true">
          <circle cx="12" cy="12" r="10" fill="#f0b91e"/>
          <g fill="none" stroke="#13365c" stroke-width="1.4">
            <ellipse cx="12" cy="12" rx="4" ry="10"/>
            <path d="M2 12h20M4 7h16M4 17h16"/>
          </g>
        </svg>
        www.wrenfielddisability.com
      </li>
    </ul>

    <address class="address">
      48 #117, Harlow<br>
      Vale 02931, United States
    </address>
  </section>

</body>
</html>
```